The Brightwater Compass Business Card

We need an attractive business card with the logo that we bought from ArtVantly last year.
Our mission is to contribute to change the way today's leaders manage business companies bringing value to the workplace and helping them to build a new model of creating wealth.
Our logo is clear about our values : we seek Positive Change through People and are convinced that the pursuit of individual well-being and the chase of economic results can converge with the right management.
Management Consulting
Corinne Fabrelle
+34 612 98 70 31
corinne.fabrelle@thebrightwatercompass-mail.net
www.thebrightwatercompass-mail.net

```html
<!DOCTYPE html>
<html lang="en">
<head>
<meta charset="utf-8">
<title>The Brightwater Compass – Business Card</title>
<link href="https://fonts.googleapis.com/css2?family=Nunito:wght@600;700;800&display=swap" rel="stylesheet">
<style>
  :root {
    --stage: #4a3440;
    --card-white: #ffffff;
    --teal: #10aaac;
    --teal-light: #1cc3c4;
    --teal-deep: #0b8385;
    --ink-teal: #0a7476;
    --white: #ffffff;
  }
  * { box-sizing: border-box; margin: 0; padding: 0; }
  html, body {
    width: 1200px; height: 800px; overflow: hidden;
    background: var(--stage);
    font-family: "Nunito", Arial, sans-serif;
  }
  .canvas {
    width: 1200px; height: 800px;
    display: flex; align-items: center; justify-content: center; gap: 40px;
  }
  .card {
    width: 540px; height: 309px;
    border-radius: 6px; position: relative; overflow: hidden;
    box-shadow: 0 10px 30px rgba(0,0,0,.35);
  }

  /* Contact side */
  .card-front { background: var(--card-white); }
  .holder-name {
    position: absolute; left: 46px; top: 92px;
    font-size: 24px; font-weight: 700; color: var(--teal);
  }
  .contact-list {
    position: absolute; left: 46px; top: 150px;
    list-style: none; display: flex; flex-direction: column; gap: 12px;
  }
  .contact-item {
    display: flex; align-items: center; gap: 10px;
    font-size: 13.5px; font-weight: 700; color: var(--ink-teal);
  }
  .contact-icon { width: 26px; height: 26px; flex: none; }
  .brand-lockup {
    position: absolute; right: 40px; top: 82px;
    display: flex; align-items: center; gap: 10px;
  }
  .brand-dot {
    width: 34px; height: 34px; border-radius: 50%;
    background: var(--teal-deep); flex: none;
  }
  .brand-name {
    font-size: 17px; font-weight: 700; line-height: 1.15;
    color: var(--ink-teal); width: 150px;
  }

  /* Brand side */
  .card-back {
    background: linear-gradient(135deg, var(--teal) 0%, var(--teal-deep) 55%, var(--teal-light) 100%);
  }
  .back-brand {
    position: absolute; left: 40px; top: 118px;
    font-size: 24px; font-weight: 700; line-height: 1.2;
    color: var(--white); width: 220px;
  }
  .back-artwork {
    position: absolute; right: 0; top: 0; width: 280px; height: 100%;
    background: radial-gradient(ellipse at 60% 50%, rgba(255,255,255,.28) 0%, rgba(255,255,255,.08) 60%, rgba(255,255,255,0) 80%);
  }
</style>
</head>
<body>
<main class="canvas">

  <section class="card card-front" aria-label="Business card, contact side">
    <h1 class="holder-name">Corinne Fabrelle</h1>

    <div class="brand-lockup">
      <span class="brand-dot" aria-hidden="true"></span>
      <span class="brand-name">The Brightwater Compass</span>
    </div>

    <ul class="contact-list">
      <li class="contact-item">
        <svg class="contact-icon" viewBox="0 0 26 26" aria-hidden="true">
          <circle cx="13" cy="13" r="13" fill="#0a7476"/>
          <path d="M9.5 7.5l2 0.3 1 2.8-1.4 1.1a7 7 0 0 0 3.2 3.2l1.1-1.4 2.8 1 .3 2a1.4 1.4 0 0 1-1.5 1.3A10 10 0 0 1 8.2 9a1.4 1.4 0 0 1 1.3-1.5z" fill="#fff"/>
        </svg>
        +34 612 98 70 31
      </li>
      <li class="contact-item">
        <svg class="contact-icon" viewBox="0 0 26 26" aria-hidden="true">
          <circle cx="13" cy="13" r="13" fill="#0a7476"/>
          <rect x="7" y="8.5" width="12" height="9" rx="1" fill="#fff"/>
          <path d="M7.5 9l5.5 4.5L18.5 9" stroke="#0a7476" stroke-width="1.2" fill="none"/>
        </svg>
        corinne.fabrelle@thebrightwatercompass-mail.net
      </li>
      <li class="contact-item">
        <svg class="contact-icon" viewBox="0 0 26 26" aria-hidden="true">
          <circle cx="13" cy="13" r="13" fill="#0a7476"/>
          <circle cx="13" cy="13" r="6" fill="none" stroke="#fff" stroke-width="1.4"/>
          <ellipse cx="13" cy="13" rx="2.6" ry="6" fill="none" stroke="#fff" stroke-width="1.2"/>
          <line x1="7" y1="13" x2="19" y2="13" stroke="#fff" stroke-width="1.2"/>
        </svg>
        www.thebrightwatercompass-mail.net
      </li>
    </ul>
  </section>

  <section class="card card-back" aria-label="Business card, brand side">
    <p class="back-brand">The Brightwater Compass</p>
    <div class="back-artwork" role="img" aria-label="Large white brand illustration area on teal"></div>
  </section>

</main>
</body>
</html>
```